Business Card Design

We're a new real estate investment company based out of West Palm Beach Florida. We buy distressed properties to fix and flip. We want the color scheme of the card to match the colors of our logo which is black and gold. We encourage all designers to be creative with the design of the card. We are not looking for a bland, boring, traditional business card. Please use legible fonts for the text as well.

Target Market(s)

Home owners, and Real Estate Investors.

Industry/Entity Type

Real Estate

Contact Information for Business Card

Dalen Vorstagg
Real Estate Investor

ESTATE FALCONS, LLC
7248 S. CORAL HAVEN WAY
SUITE 19
WEST PALM BEACH, FL. 33162
OFFICE: 1-800-555-0182
FAX: 1-888-555-0147
EMAIL: dalen@estatefalcons.example
www.estatefalcons.example

Requirements
Must have
• PLACE THESE WORDS IN BIG BOLD PRINT ON BOTH SIDES OF THE DESIGN:

WE BUY HOUSES WITH CASH!

```html
<!DOCTYPE html>
<html lang="en">
<head>
<meta charset="utf-8">
<title>Estate Falcons — Business Card</title>
<link rel="stylesheet" href="https://fonts.googleapis.com/css2?family=Open+Sans:wght@400;600;700;800&display=swap">
<style>
  :root {
    --gold: #f2d31b;
    --black: #0d0d0d;
    --white: #ffffff;
    --backdrop: #d9d9db;
    --ink: #1a1a1a;
  }
  * { box-sizing: border-box; margin: 0; padding: 0; }
  html, body {
    width: 883px; height: 1200px; overflow: hidden;
    background: var(--backdrop);
    font-family: "Open Sans", Arial, sans-serif;
  }
  .card {
    position: absolute; left: 267px; width: 390px;
    box-shadow: 0 3px 6px rgba(0,0,0,.25);
    overflow: hidden;
  }
  /* ---------- front ---------- */
  .card-front { top: 381px; height: 219px; background: var(--white); }
  .brand-front {
    position: absolute; left: 30px; top: 22px; width: 110px;
    display: flex; align-items: center; gap: 6px;
  }
  .brand-dot { width: 12px; height: 12px; border-radius: 50%; background: var(--gold); flex: none; }
  .brand-name {
    font-weight: 800; font-size: 15px; line-height: 1.05; color: var(--black);
    letter-spacing: .3px;
  }
  .name-accent { position: absolute; left: 0; top: 90px; width: 8px; height: 27px; background: var(--gold); }
  .name-bar {
    position: absolute; left: 12px; top: 90px; width: 141px; height: 16px;
    background: var(--black); color: var(--gold);
    font-weight: 600; font-size: 12px; line-height: 16px; padding-left: 8px; letter-spacing: .4px;
  }
  .job-title { position: absolute; left: 34px; top: 106px; font-size: 10px; color: var(--ink); }
  .address {
    position: absolute; left: 33px; top: 126px; font-size: 9.6px; line-height: 12.5px; color: var(--ink);
  }
  .portrait {
    position: absolute; right: 0; top: 8px; width: 162px; height: 144px;
    background: linear-gradient(180deg, #f4f4f4 0%, #e9e9e9 55%, #2a2d34 78%, #1c1e23 100%);
  }
  .contact-band {
    position: absolute; left: 0; top: 152px; width: 100%; height: 36px;
    background: var(--black); border-top: 3px solid var(--gold);
    color: var(--white); font-size: 9.6px;
  }
  .contact-col { position: absolute; top: 4px; line-height: 13px; }
  .contact-left { left: 20px; }
  .contact-right { right: 18px; text-align: right; }
  .contact-row { display: flex; align-items: center; gap: 6px; }
  .contact-right .contact-row { justify-content: flex-end; }
  .contact-row svg { width: 10px; height: 9px; flex: none; }
  .fax-mark { color: var(--gold); font-weight: 700; font-size: 9.6px; width: 10px; }
  .slogan-front {
    position: absolute; left: 0; top: 188px; width: 100%; height: 24px;
    background: var(--white); border-top: 2px solid var(--gold); border-bottom: 2px solid var(--gold);
    text-align: center; font-weight: 800; font-size: 17.5px; line-height: 20px; color: var(--black);
  }
  .front-foot { position: absolute; left: 0; top: 212px; width: 100%; height: 7px; background: var(--black); }
  /* ---------- back ---------- */
  .card-back { top: 617px; height: 202px; background: var(--black); }
  .brand-back {
    position: absolute; left: 0; top: 50px; width: 100%;
    display: flex; justify-content: center; align-items: center; gap: 10px;
  }
  .brand-back .brand-name { color: var(--gold); font-size: 26px; }
  .brand-back .brand-dot { width: 18px; height: 18px; }
  .slogan-back {
    position: absolute; left: 0; top: 160px; width: 100%; height: 31px;
    background: var(--white); border-top: 2px solid var(--gold); border-bottom: 2px solid var(--gold);
    text-align: center; font-weight: 800; font-size: 20px; line-height: 27px; color: var(--black);
  }
</style>
</head>
<body>

<section class="card card-front">
  <div class="brand-front">
    <span class="brand-dot"></span>
    <span class="brand-name">ESTATE<br>FALCONS</span>
  </div>

  <div class="name-accent"></div>
  <div class="name-bar">DALEN VORSTAGG</div>
  <div class="job-title">Real Estate Investor</div>
  <div class="address">LLC 7248 S. CORAL HAVEN WAY<br>SUITE 19 WEST PALM BEACH, FL. 33162</div>

  <div class="portrait" role="img" aria-label="Portrait photo of Dalen Vorstagg in a dark suit"></div>

  <div class="contact-band">
    <div class="contact-col contact-left">
      <div class="contact-row">
        <svg viewBox="0 0 10 9"><path d="M1 3 Q5 0 9 3 L8 4 L6.5 3 L6.5 2 L3.5 2 L3.5 3 L2 4 Z M2.5 4.5 H7.5 L8.5 8.5 H1.5 Z" fill="#f2d31b"/></svg>
        <span>1-800-555-0182</span>
      </div>
      <div class="contact-row">
        <span class="fax-mark">Fx</span>
        <span>1-888-555-0147</span>
      </div>
    </div>
    <div class="contact-col contact-right">
      <div class="contact-row">
        <span>www.estatefalcons.example</span>
        <svg viewBox="0 0 10 10"><circle cx="5" cy="5" r="4" fill="none" stroke="#f2d31b" stroke-width="1"/><ellipse cx="5" cy="5" rx="1.8" ry="4" fill="none" stroke="#f2d31b" stroke-width=".8"/><line x1="1" y1="5" x2="9" y2="5" stroke="#f2d31b" stroke-width=".8"/></svg>
      </div>
      <div class="contact-row">
        <span>dalen@estatefalcons.example</span>
        <svg viewBox="0 0 10 8"><rect x=".5" y=".5" width="9" height="7" fill="#f2d31b"/><path d="M.5 .5 L5 4.5 L9.5 .5" fill="none" stroke="#0d0d0d" stroke-width=".8"/></svg>
      </div>
    </div>
  </div>

  <div class="slogan-front">WE BUY HOUSES WITH CASH!</div>
  <div class="front-foot"></div>
</section>

<section class="card card-back">
  <div class="brand-back">
    <span class="brand-dot"></span>
    <span class="brand-name">ESTATE FALCONS</span>
  </div>
  <div class="slogan-back">WE BUY HOUSES WITH CASH!</div>
</section>

</body>
</html>
```